ultra-minimalist business card

front (black background, matte):

tarik b. hosseny
writer | photographer
get@tarikhosseny.com

back (white background, matte):

a picture speaks a thousand words;
a word draws a thousand pictures.

www.tarikhosseny.com

all text should be small (white or silver - as long as it shows against the black - on the front; black or gray - as long as it shows against the white - on the back).

feel free to get creative in terms of arrangement, alignment, and font type, but remember, the overall style is minimalist, so nothing too fancy, please.

thanks.

```html
<!DOCTYPE html>
<html lang="en">
<head>
<meta charset="utf-8">
<title>Tarik B. Hosseny — Business Card</title>
<link rel="stylesheet" href="https://fonts.googleapis.com/css2?family=Crimson+Pro:wght@400&family=Open+Sans:wght@300;400;700&display=swap">
<style>
  :root {
    --page: #ffffff;
    --card-front: #000000;
    --card-back: #ffffff;
    --ink-light: #ffffff;
    --ink-muted: #d9d9d9;
    --ink-dark: #111111;
    --ink-gray: #8a8a8a;
    --quote-mark: #cfcfcf;
    --shadow: rgba(0, 0, 0, 0.22);
  }
  * { margin: 0; padding: 0; box-sizing: border-box; }
  html, body {
    width: 976px;
    height: 1200px;
    overflow: hidden;
    background: var(--page);
  }
  .sheet {
    position: relative;
    width: 976px;
    height: 1200px;
  }
  .card {
    position: absolute;
    left: 20px;
    width: 936px;
    box-shadow: 0 6px 18px var(--shadow);
  }
  .card--front {
    top: 27px;
    height: 529px;
    background: var(--card-front);
    color: var(--ink-light);
  }
  .card--back {
    top: 642px;
    height: 533px;
    background: var(--card-back);
    color: var(--ink-dark);
  }
  .card__name {
    position: absolute;
    left: 66px;
    top: 70px;
    font-family: "Crimson Pro", Georgia, serif;
    font-weight: 400;
    font-size: 82px;
    line-height: 1;
    letter-spacing: 0.5px;
  }
  .card__role {
    position: absolute;
    left: 68px;
    top: 157px;
    font-family: "Open Sans", Arial, sans-serif;
    font-weight: 300;
    font-size: 40px;
    line-height: 1;
    color: var(--ink-light);
  }
  .card__rule {
    position: absolute;
    left: 66px;
    top: 255px;
    width: 58px;
    height: 6px;
    background: var(--ink-light);
  }
  .card__email {
    position: absolute;
    left: 66px;
    top: 426px;
    font-family: "Open Sans", Arial, sans-serif;
    font-weight: 400;
    font-size: 27px;
    line-height: 1;
    color: var(--ink-muted);
  }
  .card__marks {
    position: absolute;
    inset: 0;
    width: 936px;
    height: 533px;
  }
  .card__marks text {
    font-family: "Open Sans", Arial, sans-serif;
    font-weight: 700;
    font-size: 230px;
    fill: var(--quote-mark);
  }
  .card__quote {
    position: absolute;
    left: 0;
    right: 0;
    top: 222px;
    text-align: center;
    font-family: "Open Sans", Arial, sans-serif;
    font-weight: 400;
    font-size: 33px;
    line-height: 43px;
    color: var(--ink-dark);
  }
  .card__web {
    position: absolute;
    left: 0;
    right: 0;
    top: 462px;
    text-align: center;
    font-family: "Open Sans", Arial, sans-serif;
    font-weight: 400;
    font-size: 22px;
    line-height: 1;
    letter-spacing: 0.5px;
    color: var(--ink-gray);
  }
</style>
</head>
<body>
  <main class="sheet">
    <section class="card card--front" aria-label="Card front">
      <h1 class="card__name">Tarik b. hosseny</h1>
      <p class="card__role">writer | photographer</p>
      <div class="card__rule"></div>
      <p class="card__email">get@tarikhosseny.com</p>
    </section>

    <section class="card card--back" aria-label="Card back">
      <svg class="card__marks" viewBox="0 0 936 533" aria-hidden="true">
        <text x="80" y="362">“</text>
        <text x="760" y="441">”</text>
      </svg>
      <p class="card__quote">A Picture Speaks A Thousand Words;<br>A Word Draws A Thousand Pictures.</p>
      <p class="card__web">www.tarikhosseny.com</p>
    </section>
  </main>
</body>
</html>
```